Awesome ecommerce store banner needed!

We need a sharp, clear, strong banner for one of our subcategory pages on http://www.brixmolt.com
We'd like to incorporate the following image. We'd like the background to be gray or black. We are replacing the Wireless Intercoms banner that is orange (we hate it).
WE do like our other banners, however, so please use them as reference:
SIze: 980 x 380
Two raw images of the intercom we'd like you to encorporate have been included. Choose one or the other depending on what you think would be best. If using the single angle, please duplicate it. We want two intercoms in the banner
Simple and Clean is key:
Text: Wireless Intercoms
Text Color: Can be white/off gray
Text Style: Please keep it clean in line with the website
Background: Black/gray/white

```html
<!DOCTYPE html>
<html lang="en">
<head>
<meta charset="utf-8">
<title>Wireless Intercoms – Brixmolt</title>
<link rel="stylesheet" href="https://fonts.googleapis.com/css2?family=Fira+Sans:wght@300;700&display=swap">
<style>
  :root {
    --canvas-bg: #f4f4f4;
    --canvas-bg-light: #ffffff;
    --frame: #2b2b2b;
    --heading: #333333;
    --pattern-tone: #e6e6e6;
    --device-silver: #cfd0d2;
    --device-silver-light: #eeeeef;
    --device-black: #1f1f21;
  }
  html, body {
    margin: 0;
    padding: 0;
    overflow: hidden;
    background: var(--canvas-bg-light);
  }
  .banner {
    position: relative;
    width: 1200px;
    height: 465px;
    box-sizing: border-box;
    border: 2px solid var(--frame);
    background: linear-gradient(90deg, var(--canvas-bg) 0%, var(--canvas-bg-light) 45%, var(--canvas-bg-light) 100%);
    overflow: hidden;
  }
  .banner__pattern {
    position: absolute;
    top: 0;
    right: 0;
    width: 640px;
    height: 100%;
    background: radial-gradient(ellipse at 70% 40%, var(--pattern-tone) 0%, rgba(230,230,230,0.35) 55%, rgba(255,255,255,0) 80%);
  }
  .banner__title {
    position: absolute;
    left: 90px;
    top: 130px;
    margin: 0;
    color: var(--heading);
    font-family: "Fira Sans", Arial, sans-serif;
    line-height: 1;
  }
  .banner__title-light {
    display: block;
    font-weight: 300;
    font-size: 76px;
    letter-spacing: 0.5px;
  }
  .banner__title-bold {
    display: block;
    font-weight: 700;
    font-size: 84px;
    margin-top: 12px;
    letter-spacing: 0.5px;
  }
  .banner__product {
    position: absolute;
    left: 580px;
    top: 40px;
    width: 520px;
    height: 405px;
  }
</style>
</head>
<body>
  <div class="banner">
    <div class="banner__pattern" role="img" aria-label="Faint grey pattern of communication and technology icons"></div>

    <h1 class="banner__title">
      <span class="banner__title-light">Wireless</span>
      <span class="banner__title-bold">Intercoms</span>
    </h1>

    <svg class="banner__product" viewBox="0 0 520 405" role="img" aria-label="Photo of two silver and black wireless intercom units with antennas">
      <defs>
        <linearGradient id="device-tone" x1="0" y1="0" x2="1" y2="0">
          <stop offset="0" stop-color="var(--device-silver-light)"/>
          <stop offset="0.55" stop-color="var(--device-silver)"/>
          <stop offset="0.62" stop-color="var(--device-black)"/>
          <stop offset="1" stop-color="var(--device-black)"/>
        </linearGradient>
      </defs>
      <rect x="8" y="119" width="294" height="148" rx="22" fill="url(#device-tone)"/>
      <rect x="173" y="217" width="337" height="184" rx="24" fill="url(#device-tone)"/>
    </svg>
  </div>
</body>
</html>
```